BrimFalcon Business Cards

We have a defined brand. Please visit our website to get a feel for the product and the color pallets. www.brimfalcon-demo.com

We need an updated, world class business card design. (See the attached existing card design). Please utilize BOTH sides of the card as shown and be creative with the layout. I do want the horse head icon to be positioned as it is with the existing card.

The remainder of the layout can be customized and I also want it vertically oriented.

Attached are the logo files and please use the colors as follows:
Green - #A5CE39
Tan - #CDBD99
Black

Feel free to play with the colors.

```html
<!DOCTYPE html>
<html lang="en">
<head>
<meta charset="utf-8">
<title>BrimFalcon Business Cards – Proposal 1</title>
<link rel="stylesheet" href="https://fonts.googleapis.com/css2?family=Jost:wght@400;500&display=swap">
<style>
  :root {
    --page: #ffffff;
    --ink: #111111;
    --tan: #cac594;
    --tan-shade: #bcb88a;
    --green: #99ff00;
    --green-shade: #84dd00;
  }
  * { margin: 0; padding: 0; box-sizing: border-box; }
  html, body {
    width: 848px;
    height: 1200px;
    overflow: hidden;
    background: var(--page);
  }
  body {
    position: relative;
    font-family: "Jost", "Futura", sans-serif;
    color: var(--ink);
  }
  .proposal-label {
    position: absolute;
    top: 42px;
    right: 53px;
    font-size: 15px;
    font-weight: 400;
    letter-spacing: 0.2px;
  }
  .card {
    position: absolute;
    left: 280px;
    width: 329px;
    height: 205px;
    overflow: hidden;
  }
  .card--front { top: 383px; background: var(--tan); }
  .card--back  { top: 613px; background: var(--green); }

  .card__emblem-area {
    position: absolute;
    left: -70px;
    top: -10px;
    width: 230px;
    height: 230px;
    border-radius: 50%;
  }
  .card--front .card__emblem-area { background: var(--tan-shade); }
  .card--back  .card__emblem-area { background: var(--green-shade); }

  .brand {
    position: absolute;
    top: 38px;
    right: 18px;
    display: flex;
    align-items: center;
    gap: 6px;
  }
  .brand__dot {
    width: 16px;
    height: 16px;
    border-radius: 50%;
    background: var(--ink);
  }
  .brand__name {
    font-size: 17px;
    font-weight: 500;
    color: var(--ink);
  }

  .identity {
    position: absolute;
    left: 0;
    width: 330px;
    top: 79px;
    text-align: center;
  }
  .identity__name {
    font-size: 16.5px;
    font-weight: 500;
    line-height: 20px;
  }
  .identity__title {
    font-size: 15.5px;
    font-weight: 400;
    line-height: 19px;
  }

  .contact {
    position: absolute;
    left: 17px;
    top: 132px;
    list-style: none;
  }
  .contact__item {
    display: flex;
    align-items: center;
    gap: 5px;
    height: 16px;
    font-size: 13px;
    line-height: 16px;
    white-space: nowrap;
  }
  .contact__icon {
    width: 11px;
    height: 11px;
    flex: none;
  }
</style>
</head>
<body>
  <div class="proposal-label">PROPOSAL 1</div>

  <section class="card card--front" aria-label="Card front">
    <div class="card__emblem-area" role="img" aria-label="Large faint brand emblem decoration"></div>
    <div class="brand">
      <span class="brand__dot"></span>
      <span class="brand__name">BrimFalcon</span>
    </div>
    <div class="identity">
      <p class="identity__name">Owen Darrow</p>
      <p class="identity__title">President and CEO</p>
    </div>
  </section>

  <section class="card card--back" aria-label="Card back">
    <div class="card__emblem-area" role="img" aria-label="Large faint brand emblem decoration"></div>
    <div class="brand">
      <span class="brand__dot"></span>
      <span class="brand__name">BrimFalcon</span>
    </div>
    <div class="identity">
      <p class="identity__name">Owen Darrow</p>
      <p class="identity__title">President and CEO</p>
    </div>
    <ul class="contact">
      <li class="contact__item">
        <svg class="contact__icon" viewBox="0 0 24 24"><path fill="#111" d="M6.6 10.8a15.2 15.2 0 0 0 6.6 6.6l2.2-2.2a1 1 0 0 1 1-.25 11.4 11.4 0 0 0 3.6.57 1 1 0 0 1 1 1V20a1 1 0 0 1-1 1A17 17 0 0 1 3 4a1 1 0 0 1 1-1h3.5a1 1 0 0 1 1 1c0 1.25.2 2.45.57 3.57a1 1 0 0 1-.25 1z"/></svg>
        555.010.4821
      </li>
      <li class="contact__item">
        <svg class="contact__icon" viewBox="0 0 24 24" fill="none" stroke="#111" stroke-width="2"><circle cx="12" cy="12" r="10"/><ellipse cx="12" cy="12" rx="4.5" ry="10"/><path d="M2 12h20M4 7h16M4 17h16"/></svg>
        brimfalconlabs.com
      </li>
      <li class="contact__item">
        <svg class="contact__icon" viewBox="0 0 24 24" fill="none" stroke="#111" stroke-width="2"><rect x="2" y="5" width="20" height="14"/><path d="M2 5l10 8 10-8M2 19l7-7M22 19l-7-7"/></svg>
        owen@brimfalcon.com
      </li>
      <li class="contact__item">
        <svg class="contact__icon" viewBox="0 0 24 24" fill="none" stroke="#111" stroke-width="2"><path d="M12 22s7-7.2 7-12.5a7 7 0 0 0-14 0C5 14.8 12 22 12 22z"/><circle cx="12" cy="9.5" r="2.7"/></svg>
        Fenwick, Cedarvale Province
      </li>
    </ul>
  </section>
</body>
</html>
```